Business Card for Makeup Artist

I need a business card designed for my makeup and hair artistry business which is primarily events and weddings focused. The card needs to be sleek, simple, stylish and appealing to women. I would prefer a white background but open to suggestions also. I also love the marble background look. I have attached some example pics. It needs to be a double sided card with logo and/or design on one side and contact details in the centre of the card on the other side. NO LOGO ON BACK. Examples attached.

Target Market(s)

Females age 14-55

Industry/Entity Type

Business

Contact Information for Business Card

Nora Vint
Principal Makeup Artist
P: 0413 925 214
E: nora@lumirabeauty.com.au
W: www.lumirabeauty.com.au

Requirements
Should not have
• No yellow, green, red or blue in the design.

```html
<!DOCTYPE html>
<html lang="en">
<head>
<meta charset="utf-8">
<title>Lumira Makeup Artistry – Business Card</title>
<link rel="stylesheet" href="https://fonts.googleapis.com/css2?family=Open+Sans:wght@400;600&display=swap">
<style>
  :root {
    --bg: #e9e6e3;
    --card: #141414;
    --brand-grey: #8a8a8a;
    --name-grey: #9b9b9b;
    --pink: #e04fc0;
    --text: #f2f2f2;
    --divider: #4a4a4a;
  }
  * { box-sizing: border-box; margin: 0; padding: 0; }
  html, body {
    width: 1200px; height: 814px; overflow: hidden;
    background: var(--bg);
    font-family: "Open Sans", sans-serif;
  }
  .sheet {
    position: relative; width: 1200px; height: 814px;
    display: flex; align-items: center; justify-content: center; gap: 40px;
  }
  .card {
    width: 540px; height: 300px;
    background: var(--card);
    border-radius: 3px;
    box-shadow: 0 10px 30px rgba(0,0,0,.25);
    position: relative;
    overflow: hidden;
  }
  /* Contact side */
  .card--contact { display: flex; align-items: center; }
  .card--contact .brand {
    width: 260px; padding-left: 44px;
    color: var(--brand-grey);
    font-weight: 400;
  }
  .brand__name { font-size: 40px; line-height: 1; letter-spacing: 1px; display: block; }
  .brand__line { font-size: 15px; letter-spacing: 2px; text-transform: uppercase; display: block; margin-top: 6px; }
  .divider {
    width: 1px; height: 120px; background: var(--divider); margin: 0 22px 0 6px;
  }
  .contact__name { color: var(--name-grey); font-size: 15px; font-weight: 600; }
  .contact__role { color: var(--pink); font-size: 14px; margin-bottom: 8px; }
  .contact__list { list-style: none; }
  .contact__item {
    display: flex; align-items: center; gap: 9px;
    color: var(--text); font-size: 13.5px; line-height: 21px;
  }
  .contact__item svg { width: 12px; height: 12px; fill: var(--brand-grey); flex: none; }
  /* Logo side */
  .card--logo {
    display: flex; flex-direction: column; align-items: center; justify-content: center;
  }
  .card--logo .brand { color: var(--brand-grey); text-align: center; font-weight: 400; margin-top: -20px; }
  .card--logo .brand__name { font-size: 62px; }
  .card--logo .brand__line { font-size: 20px; letter-spacing: 3px; }
  .website {
    color: var(--text); font-size: 13px; letter-spacing: 2px; margin-top: 44px;
  }
</style>
</head>
<body>
<main class="sheet">
  <section class="card card--contact">
    <div class="brand">
      <span class="brand__name">Lumira</span>
      <span class="brand__line">Makeup Artistry</span>
    </div>
    <div class="divider"></div>
    <div class="contact">
      <p class="contact__name">Nora Vint</p>
      <p class="contact__role">Principal Makeup Artist</p>
      <ul class="contact__list">
        <li class="contact__item">
          <svg viewBox="0 0 24 24" aria-hidden="true"><path d="M6.6 10.8a15.1 15.1 0 0 0 6.6 6.6l2.2-2.2a1 1 0 0 1 1-.25 11.4 11.4 0 0 0 3.6.57 1 1 0 0 1 1 1V20a1 1 0 0 1-1 1A17 17 0 0 1 3 4a1 1 0 0 1 1-1h3.5a1 1 0 0 1 1 1c0 1.25.2 2.45.57 3.57a1 1 0 0 1-.25 1z"/></svg>
          0413 925 214
        </li>
        <li class="contact__item">
          <svg viewBox="0 0 24 24" aria-hidden="true"><path d="M2 5h20v14H2zm2 2v.5l8 5 8-5V7zm0 2.8V17h16V9.8l-8 5z"/></svg>
          nora@lumirabeauty.com.au
        </li>
        <li class="contact__item">
          <svg viewBox="0 0 24 24" aria-hidden="true"><path d="M12 2a10 10 0 1 0 0 20 10 10 0 0 0 0-20zm6.9 6h-2.9a15.6 15.6 0 0 0-1.4-3.6A8 8 0 0 1 18.9 8zM12 4c.8 1.2 1.5 2.5 1.9 4h-3.8c.4-1.5 1.1-2.8 1.9-4zM4.3 14a8 8 0 0 1 0-4h3.4a16.5 16.5 0 0 0 0 4zm.8 2h2.9c.3 1.3.8 2.5 1.4 3.6A8 8 0 0 1 5.1 16zM8 8H5.1a8 8 0 0 1 4.3-3.6C8.8 5.5 8.3 6.7 8 8zm4 12c-.8-1.2-1.5-2.5-1.9-4h3.8c-.4 1.5-1.1 2.8-1.9 4zm2.3-6H9.7a14.7 14.7 0 0 1 0-4h4.6a14.7 14.7 0 0 1 0 4zm.3 5.6c.6-1.1 1.1-2.3 1.4-3.6h2.9a8 8 0 0 1-4.3 3.6zm1.7-5.6a16.5 16.5 0 0 0 0-4h3.4a8 8 0 0 1 0 4z"/></svg>
          www.lumirabeauty.com.au
        </li>
      </ul>
    </div>
  </section>

  <section class="card card--logo">
    <div class="brand">
      <span class="brand__name">Lumira</span>
      <span class="brand__line">Makeup Artistry</span>
    </div>
    <p class="website">www.lumirabeauty.com.au</p>
  </section>
</main>
</body>
</html>
```